Brindlemoor Client Journey To Success

I need a one-page document that graphically shows the client's journey working with Brindlemoor from initial assessment to completed project. I want the journey to start at the "basecamp logo" and reach 4 summits (little mountain logos...) .

I'd like the imagery to convey the client starting at basecamp, and moving to each summit. Each summit, should list the subtext under each, as listed on the pdf doc i provided.

The description for the basecamp and 4 summits is attached.

I need the brochure to look like the other brochure that you did for me (attached) .

Target Market(s)

Restaurant Owners

Industry/Entity Type

Construction Management

Font styles to use
Sans Serif

Colors
EB3D1F
EC4F4E
F09395
F8D3D4
FCEDEE

Requirements
Must have
• My logo. Title: Client Journey To Success. Subtitle: The 4 Summits

```html
<!DOCTYPE html>
<html lang="en">
<head>
<meta charset="utf-8">
<title>Brindlemoor Development – Client Journey To Success</title>
<link href="https://fonts.googleapis.com/css2?family=Montserrat:ital,wght@0,400;0,500;0,700;0,800;0,900;1,400&display=swap" rel="stylesheet">
<style>
  :root{
    --stage:#111111;
    --paper:#f4f4f4;
    --red:#d7312f;
    --red-deep:#b8221f;
    --ink:#1d1d1d;
    --ink-soft:#444444;
    --header-dark:#3a3b3d;
    --header-mid:#5d6063;
    --white:#ffffff;
  }
  *{box-sizing:border-box;margin:0;padding:0}
  html,body{width:1200px;height:942px;overflow:hidden;background:var(--stage)}
  body{font-family:"Montserrat",sans-serif;color:var(--ink)}
  .flyer{position:absolute;left:280px;top:18px;width:640px;height:906px;background:var(--paper);overflow:hidden;box-shadow:0 10px 40px rgba(0,0,0,.6)}
  .abs{position:absolute}

  .header-photo{left:0;top:0;width:640px;height:250px;background:linear-gradient(135deg,var(--header-mid),var(--header-dark))}
  .logo-panel{left:0;top:58px;width:300px;height:200px;background:var(--paper);border-top-right-radius:60px}
  .brand{left:34px;top:120px;display:flex;align-items:center;gap:10px}
  .brand-mark{width:26px;height:26px;background:var(--red)}
  .brand-name{font-weight:800;font-size:15px;color:var(--ink);text-transform:uppercase;letter-spacing:.3px}

  .title{right:26px;top:26px;width:340px;text-align:right;color:var(--white);font-weight:900;font-size:38px;line-height:1.05;text-transform:uppercase}
  .summits-banner{left:300px;top:160px;width:340px;height:90px}
  .summits-text{left:300px;top:168px;width:340px;text-align:center;color:var(--white);font-weight:900;font-size:24px;line-height:1;text-transform:uppercase}

  .basecamp{left:34px;top:272px}
  .basecamp h2{color:var(--red);font-weight:900;font-size:34px;text-transform:uppercase;letter-spacing:.5px}
  .basecamp ol{list-style:none;margin-top:4px}
  .basecamp li{font-weight:800;font-size:16px;line-height:1.3}

  .stage-block{width:270px}
  .tab{display:inline-block;background:var(--red);color:var(--white);font-size:11px;font-weight:500;padding:2px 14px 2px 8px;border-top-right-radius:10px}
  .stage-block h3{font-weight:700;font-size:21px;line-height:1.15;padding-bottom:2px;border-bottom:2px solid var(--ink)}
  .stage-block ol{list-style:none;margin-top:3px}
  .stage-block li{font-size:11.5px;line-height:1.3;color:var(--ink-soft)}
  .stage-block.major h3{font-size:22px}

  .s1{left:40px;top:408px}
  .s2{left:340px;top:270px}
  .s3{left:340px;top:368px;width:285px}
  .s4{left:340px;top:502px}

  .divider{left:326px;top:270px;width:2px;height:320px;background:#c9c9c9}

  .photo{background:linear-gradient(135deg,#8a2a24,#c9503a 55,#3a2a24)}
  .photo-a{left:22px;top:600px;width:240px;height:120px;background:linear-gradient(135deg,#b8322a,#5a2f2a)}
  .photo-b{left:246px;top:628px;width:210px;height:130px;background:linear-gradient(135deg,#e0a060,#b86a2a)}
  .photo-c{left:412px;top:690px;width:208px;height:150px;background:linear-gradient(135deg,#3a3030,#b93a30 60%,#d8a070)}

  .web-band{left:0;top:742px;width:640px;height:70px;background:var(--red)}
  .web{left:40px;top:764px;color:var(--white);font-weight:700;font-size:21px}
  .foot-band{left:0;top:862px;width:640px;height:22px;background:var(--red)}
</style>
</head>
<body>
  <main class="flyer">
    <div class="abs header-photo" role="img" aria-label="Photo of a construction crew in hi-vis vests on site"></div>
    <div class="abs logo-panel"></div>
    <div class="abs brand">
      <span class="brand-mark"></span>
      <span class="brand-name">Brindlemoor Development</span>
    </div>

    <h1 class="abs title">Client Journey<br>To Success</h1>
    <svg class="abs summits-banner" viewBox="0 0 340 90" aria-hidden="true">
      <polygon points="0,0 340,0 340,46 170,86 0,46" fill="var(--red)"/>
      <polyline points="0,52 170,92 340,52" fill="none" stroke="var(--ink)" stroke-width="4"/>
    </svg>
    <p class="abs summits-text">The 4<br>Summits</p>

    <section class="abs basecamp">
      <h2>Basecamp</h2>
      <ol>
        <li>a. Client Assessment</li>
        <li>b. Determine Project Goals</li>
        <li>c. Proposal &amp; Fees</li>
      </ol>
    </section>

    <div class="abs divider"></div>

    <section class="abs stage-block s1">
      <span class="tab">Summit 1</span>
      <h3>PreConstruction</h3>
      <ol>
        <li>a. Develop Project Plan</li>
        <li>b. Develop Risk Assessment &amp; Plan</li>
        <li>c. Develop Schedule</li>
        <li>d. Develop Budget</li>
        <li>e. Develop Team</li>
        <li>f. GC, Sub, Consultants Contracts</li>
      </ol>
    </section>

    <section class="abs stage-block s2">
      <span class="tab">Summit 2</span>
      <h3>Execution</h3>
      <ol>
        <li>a. Acquire Permits</li>
        <li>b. PreConstruction Meeting</li>
        <li>c. Project Start</li>
      </ol>
    </section>

    <section class="abs stage-block major s3">
      <span class="tab">Summit 3</span>
      <h3>Project Management</h3>
      <ol>
        <li>a. Shared Consciousness Meetings</li>
        <li>b. Pressurized Collaboration</li>
        <li>c. Schedule Management</li>
        <li>d. Run O.O.D.A. Loop</li>
      </ol>
    </section>

    <section class="abs stage-block major s4">
      <span class="tab">Summit 4</span>
      <h3>Completion</h3>
      <ol>
        <li>a. Closeout</li>
      </ol>
    </section>

    <div class="abs web-band"></div>
    <div class="abs photo-a" role="img" aria-label="Photo of a restaurant dining room with red walls"></div>
    <div class="abs photo-b" role="img" aria-label="Photo of a warm wood-toned restaurant interior"></div>
    <div class="abs photo-c" role="img" aria-label="Photo of a finished restaurant bar with neon sign"></div>
    <p class="abs web">www.brindlemoorbuild.com</p>
    <div class="abs foot-band"></div>
  </main>
</body>
</html>
```